Cover für Notfallordner zur Aufbewahrung von wichtigen Dokumenten
Zielgruppe
Wir sind eigentlich eine Veltaro Agentur.
Hier geht es aber um die Gestaltung eines 'Notfallordners', der zur Aufbewahrung von Patientenverfügung, Vorsorgevollmacht, Testament etc. dienen soll.
Die Ordner Außenseite soll einfach gestaltet werden mit der Aufschrift 'Notfallordner'
Aufgabenstellung
Farbe: bitte denken Sie sich etwas aus,gerne aber nicht in Rot sondern dunklem grün
Idee habe ich im Anhang beigefügt, soll aber eine eigene 'Variante' werden, die nicht nach 'abgekupfert aussieht'.
Wenig Grafik/Design, schlicht

```html
<!DOCTYPE html>
<html lang="de">
<head>
<meta charset="utf-8">
<title>Notfallordner – Cover und Rücken</title>
<link rel="stylesheet" href="https://fonts.googleapis.com/css2?family=Roboto+Condensed:wght@500&display=swap">
<style>
  :root {
    --page-bg: #ffffff;
    --green-deep: #0c3f30;
    --green-main: #15573f;
    --arc-tint: rgba(255, 255, 255, 0.07);
    --ink-white: #ffffff;
  }
  * { margin: 0; padding: 0; box-sizing: border-box; }
  html, body {
    width: 727px;
    height: 1200px;
    overflow: hidden;
    background: var(--page-bg);
  }
  .binder-layout {
    position: relative;
    width: 727px;
    height: 1200px;
  }
  .spine, .front-cover {
    position: absolute;
    top: 290px;
    height: 621px;
    overflow: hidden;
    background: linear-gradient(165deg, var(--green-main) 0%, var(--green-main) 40%, var(--green-deep) 100%);
  }
  .spine { left: 62px; width: 81px; }
  .front-cover { left: 195px; width: 505px; }
  .arcs {
    position: absolute;
    inset: 0;
    width: 100%;
    height: 100%;
  }
  .brand-lockup {
    position: absolute;
    display: flex;
    color: var(--ink-white);
    font-family: "Roboto Condensed", "Arial Narrow", sans-serif;
    font-weight: 500;
  }
  .brand-mark {
    display: block;
    flex: none;
    border: 4px solid var(--ink-white);
    border-radius: 6px;
  }
  .brand-word {
    display: flex;
    flex-direction: column;
    line-height: 1;
    letter-spacing: 0.5px;
  }
  /* Front: square mark left, two-line wordmark right */
  .front-cover .brand-lockup { left: 88px; top: 432px; align-items: flex-end; gap: 18px; }
  .front-cover .brand-mark { width: 134px; height: 134px; }
  .front-cover .brand-word { font-size: 50px; padding-bottom: 4px; }
  /* Spine: square on top, wordmark running downwards */
  .spine .brand-lockup {
    left: 0;
    right: 0;
    top: 14px;
    flex-direction: column;
    align-items: center;
    gap: 8px;
  }
  .spine .brand-mark { width: 30px; height: 30px; border-width: 3px; border-radius: 4px; }
  .spine .brand-word { writing-mode: vertical-rl; font-size: 19px; line-height: 1.05; }
</style>
</head>
<body>
<main class="binder-layout">

  <section class="spine" aria-label="Ordnerrücken">
    <svg class="arcs" viewBox="0 0 81 621" preserveAspectRatio="none" aria-hidden="true">
      <circle cx="400" cy="640" r="520" fill="var(--arc-tint)"/>
      <circle cx="-70" cy="20" r="160" fill="var(--arc-tint)"/>
    </svg>
    <div class="brand-lockup">
      <span class="brand-mark" aria-hidden="true"></span>
      <div class="brand-word"><span>NOTFALL</span><span>ORDNER</span></div>
    </div>
  </section>

  <section class="front-cover" aria-label="Ordnervorderseite">
    <svg class="arcs" viewBox="0 0 505 621" preserveAspectRatio="none" aria-hidden="true">
      <circle cx="560" cy="700" r="580" fill="var(--arc-tint)"/>
      <circle cx="-40" cy="-40" r="170" fill="var(--arc-tint)"/>
    </svg>
    <div class="brand-lockup">
      <span class="brand-mark" aria-hidden="true"></span>
      <div class="brand-word"><span>NOTFALL</span><span>ORDNER</span></div>
    </div>
  </section>

</main>
</body>
</html>
```